Tarnwick Growth Systems Wordpress Design

We need a design for a company that focuses on Data Driven Marketing Technology Solutions. We have an existing web site (www.tarnwickgrowsys.example) that needs to be totally replaced. I want to keep certain elements of the site layout (e.g. menus, menu bar email signup), but I don't like the content in the sliders (sliders are not a requirement). I want to keep the blog, but again want a more professional looking presentation for the blog. I also want to add my twitter feed to the home page. I also want to create a professional pages that better articulates what we do from a services perspective. Web site should use colors from the attached logo although I'm open to a different color palate. Web site should communicate a data and technology focus on marketing and customer engagement. From a design perspective I want this to be extensible (e.g. standard WP plugins) and I really want a clean, simple, well performing CSS scheme. I think we are talking about 4 pages here. The pages would include a home page, a services pages (see attached), an About Me page, and a landing pages for email subscriptions. See http://plumelinestudio.example/ and http://www.quillharborworks.example/#who-is-quillharbor for an example of sites I like.

```html
<!DOCTYPE html>
<html lang="en">
<head>
<meta charset="utf-8">
<title>Tarnwick Growth Systems</title>
<link rel="stylesheet" href="https://fonts.googleapis.com/css2?family=Open+Sans:wght@400;600;700&display=swap">
<style>
:root{
  --orange:#e0942b;
  --orange-dark:#c97f1c;
  --ink:#333333;
  --muted:#777777;
  --line:#e4e4e4;
  --band:#2b3440;
  --footer:#3b3b3b;
  --white:#ffffff;
}
*{box-sizing:border-box;margin:0;padding:0}
html,body{width:1200px;height:2204px;overflow:hidden}
body{font-family:"Open Sans",Arial,sans-serif;color:var(--ink);background:var(--white);position:relative}
.wrap{width:1016px;margin:0 auto;position:relative}

.topbar{height:30px;background:var(--white);border-bottom:1px solid var(--line);font-size:12px;color:var(--muted)}
.topbar .wrap{display:flex;justify-content:flex-end;align-items:center;height:30px}

.header{height:170px;position:relative;border-bottom:1px solid var(--line)}
.brand{position:absolute;left:32px;top:58px;display:flex;align-items:center;gap:12px}
.brand-mark{width:54px;height:54px;border-radius:50%;background:var(--orange)}
.brand-name{font-size:22px;font-weight:700;color:var(--ink);line-height:1.1;width:150px}
.signup{position:absolute;right:92px;top:56px;display:flex;gap:8px}
.signup-input{width:200px;height:40px;border:1px solid #cfcfcf;font-size:12px;color:#888;padding:0 12px;display:flex;align-items:center}
.signup-btn{width:92px;height:40px;background:var(--orange);color:var(--white);font-size:13px;display:flex;align-items:center;justify-content:center}
.nav{position:absolute;right:92px;top:138px;display:flex;gap:34px;font-size:14px}
.nav a{color:var(--ink);text-decoration:none;padding-bottom:8px}
.nav a.active{color:var(--orange);border-bottom:3px solid var(--orange)}

.hero{height:420px;background:linear-gradient(180deg,#dfe4ea 0%,#c9d2dc 45%,#8e7e70 70%,#4a3a30 100%)}

.section-head{display:flex;justify-content:space-between;align-items:center;padding-top:50px;margin-bottom:30px}
.section-head h2{font-size:36px;font-weight:600;color:var(--ink)}
.arrows{display:flex;gap:6px}
.arrows span{width:26px;height:26px;background:#555;display:flex;align-items:center;justify-content:center}

.services{height:532px}
.service-grid{display:flex;gap:20px}
.service-card{width:239px;height:356px}
.service-card.feature{background:var(--orange);color:var(--white);text-align:center;padding:44px 22px 0;border:8px solid #edb062}
.service-card.feature h3{font-size:22px;font-weight:600;line-height:1.35;margin-bottom:20px}
.service-card.feature p{font-size:11px;line-height:1.6;margin-bottom:26px}
.btn-light{display:inline-block;border:1px solid var(--white);padding:8px 20px;font-size:12px}
.photo-a{background:linear-gradient(135deg,#2f3640,#8b97a3 60%,#c9cfd5)}
.photo-b{background:linear-gradient(160deg,#d9dde2,#3c5f86 55%,#1c2530)}
.photo-c{background:linear-gradient(180deg,#4c5560,#6d7884 60%,#2d333a)}

.difference{height:296px;background:linear-gradient(180deg,#3b4654 0%,var(--band) 60%,#1e252d 100%);color:var(--white);text-align:center;padding-top:54px}
.difference h2{font-size:36px;font-weight:400;margin-bottom:20px}
.difference p{width:900px;margin:0 auto 28px;font-size:12px;line-height:1.7;color:#dfe3e8}
.btn-outline{display:inline-block;border:1px solid var(--white);padding:12px 22px;font-size:13px}

.blog{height:544px}
.blog-grid{display:flex;gap:28px}
.post{width:320px}
.post-img{height:212px;margin-bottom:16px}
.img-1{background:linear-gradient(135deg,#cfd8e0,#6f8396 55%,#2e3b48)}
.img-2{background:linear-gradient(135deg,#e6eaee,#8aa0b4 50%,#445567)}
.img-3{background:linear-gradient(135deg,#1b2b44,#3f73b3 50%,#c7a75d)}
.post h3{font-size:14px;font-weight:600;color:var(--orange);line-height:1.45;margin-bottom:6px}
.post .date{font-size:11px;color:var(--muted);margin-bottom:10px}
.post p{font-size:12px;color:var(--muted);line-height:1.6;margin-bottom:8px}
.post .more{font-size:12px;color:var(--orange)}

.tweets{height:100px;background:var(--orange)}
.tweets .wrap{display:flex;align-items:center;gap:24px;height:100px}
.tweet-icon{width:44px;height:44px;border-radius:50%;background:var(--white);flex:none}
.tweets p{font-size:12px;color:var(--white);line-height:1.6}

.footer{height:112px;background:var(--footer);color:#d0d0d0;text-align:center;padding-top:30px}
.footer nav{display:flex;justify-content:center;gap:36px;font-size:13px;color:var(--white);margin-bottom:14px}
.footer small{font-size:11px}
.to-top{position:absolute;right:20px;bottom:16px;width:22px;height:22px}
</style>
</head>
<body>

<div class="topbar"><div class="wrap">Call Us: (555) 014-2280 &nbsp;|&nbsp; hello@tarnwickgrowsys.example</div></div>

<header class="header">
  <div class="brand"><span class="brand-mark"></span><span class="brand-name">Tarnwick Growth Systems</span></div>
  <div class="signup"><div class="signup-input">Enter Your Email ID</div><div class="signup-btn">Subscribe</div></div>
  <nav class="nav">
    <a class="active">Home</a><a>About us</a><a>Services</a><a>Blogs</a><a>Free Tech Assessment</a><a>Contact Us</a>
  </nav>
</header>

<section class="hero" role="img" aria-label="Photo of business people seated at a boardroom table facing a large window"></section>

<section class="services"><div class="wrap">
  <div class="section-head"><h2>Our Services</h2>
    <div class="arrows">
      <span><svg width="10" height="10" viewBox="0 0 10 10"><path d="M7 1 3 5l4 4" stroke="#fff" stroke-width="1.6" fill="none"/></svg></span>
      <span><svg width="10" height="10" viewBox="0 0 10 10"><path d="M3 1l4 4-4 4" stroke="#fff" stroke-width="1.6" fill="none"/></svg></span>
    </div>
  </div>
  <div class="service-grid">
    <div class="service-card feature">
      <h3>Data Quality /<br>Stewardship</h3>
      <p>Clean customer data is the foundation of every campaign. We audit, repair and govern your records so your teams can act with confidence on every insight.</p>
      <span class="btn-light">Read more</span>
    </div>
    <div class="service-card photo-a" role="img" aria-label="Photo of hands typing on a laptop keyboard"></div>
    <div class="service-card photo-b" role="img" aria-label="Photo of a laptop showing colourful analytics charts"></div>
    <div class="service-card photo-c" role="img" aria-label="Photo of a businessman facing a wall of sketched diagrams"></div>
  </div>
</div></section>

<section class="difference" role="region" aria-label="Why we are different">
  <h2>Why we are Different</h2>
  <p>We are different from traditional digital marketing agencies in that our focus is on long-term marketing technology strategy over one-off programs. We make sure that your marketing infrastructure and data is fundamentally sound so that investments in individual programs generate the best returns.</p>
  <span class="btn-outline">Request a Free Tech Assessment</span>
</section>

<section class="blog"><div class="wrap">
  <div class="section-head"><h2>Recent Blog</h2>
    <div class="arrows">
      <span><svg width="10" height="10" viewBox="0 0 10 10"><path d="M7 1 3 5l4 4" stroke="#fff" stroke-width="1.6" fill="none"/></svg></span>
      <span><svg width="10" height="10" viewBox="0 0 10 10"><path d="M3 1l4 4-4 4" stroke="#fff" stroke-width="1.6" fill="none"/></svg></span>
    </div>
  </div>
  <div class="blog-grid">
    <article class="post">
      <div class="post-img img-1" role="img" aria-label="Photo of a professional working at a laptop in an office"></div>
      <h3>Don't Alienate your best customers, Do you know who they are?</h3>
      <div class="date">June 11, 2015</div>
      <p>Many customer experiences can be easily improved by making customer data actionable.</p>
      <div class="more">Read More</div>
    </article>
    <article class="post">
      <div class="post-img img-2" role="img" aria-label="Photo of a man reviewing data on a desktop computer"></div>
      <h3>Essential Strategies for Measuring Marketing Effectiveness</h3>
      <div class="date">June 11, 2015</div>
      <p>Many customer experiences can be easily improved by making customer data actionable.</p>
      <div class="more">Read More</div>
    </article>
    <article class="post">
      <div class="post-img img-3" role="img" aria-label="Illustration of glowing technology icons around a hand"></div>
      <h3>5 Tips for Flawless Preference Management</h3>
      <div class="date">June 11, 2015</div>
      <p>Many customer experiences can be easily improved by making customer data actionable.</p>
      <div class="more">Read More</div>
    </article>
  </div>
</div></section>

<section class="tweets"><div class="wrap">
  <span class="tweet-icon"></span>
  <p>Keep your audience on your list: short reads on smarter data, cleaner segments and better engagement. Latest post: http://plumelinestudio.example/ shows how tidy preference centres lift retention without extra spend.</p>
</div></section>

<footer class="footer">
  <nav><span>Home</span><span>About us</span><span>Services</span><span>Blogs</span><span>Free Tech Assessment</span><span>Contact Us</span></nav>
  <small>© 2015 tarnwickgrowsys.example. All rights reserved.</small>
  <svg class="to-top" viewBox="0 0 22 22"><path d="M5 14l6-6 6 6" stroke="#e0942b" stroke-width="2" fill="none"/></svg>
</footer>

</body>
</html>
```